Biker App Design
Zielgruppe
VeloMarn erstellt eine App für Biker mit der:
- Motorradfahrer andere Biker finden können um gemeinsam zu fahren
- Motorradfahrer ihre Strecke tracken können um Punkte zu sammeln
- Biker können mit diesen Punkten Ränge aufsteigen 'Masterbiker, Anfänger, GuruFahrer, etc.', es soll eine Art 'Erfahrungsleiste' angezeigt werden
- Diese Punkte können gegen Gutscheine/Wertsachen eingelöst werden
- Es gibt Nachrichten (Art Blogeinträge) genau zu diesen Themen
Aufgabenstellung
Modernes Design
Reduziert
Es werden folgende Screens benötigt:
Startbild
Start - Dateneintragen:
Um den Fahrer besser mit anderen Fahren zu verknüpfen muss er folgende informationen angeben:
- Welche Art Motorrad fährt er? Sport, Vintage, Cross
- Männlich/Weiblich/Divers
- Geburtsjahr
- PLZ des Heimatorts
- Nickname
Startscreen um andere Biker zu suchen und damit eine Tour zu starten
- Hier sollte ein 'Map' Bild mit einem Kreis für den Umkreis dargestellt werden + Pins mit Personenbilder , welche
Personen in der Nähe sind und auch fahren möchten
- Hier sollte stehen, wieviel Punkte er noch benötigt um den nächsten Gutschein freizuschalten
Screen zum Start des Trackens
Screen während dem Tracken mit Pause/Stop-Option
Screen mit einem Überblick der neuen Blogeinträge
Screen beim beenden des Trackens (Strecke speichern, Bild hinzufügen, Freunde informieren ich bin angekommen)
Screen Profilseite, Bild des Bikers + Bike + Erfahrungspunkte + gesammelte Errungenschaften z.B. 'Mit 3 Freunden mehr als 1000km gefahren'
Screen Bestenliste, anhand der Punkte
Es sollen Dateiformate verwendet werden, die gut wiederverwendet werden können. Es sollen sich Bausteine aus diesen Design wiederverwenden lassen können.
Wir benötigen eine APP mit einem User-Dashboards (Life-Account) in dem Finanz, Karriere und Gesundheitsthemen erkennbar sein sollen. Look and Feel soll seriös, schnörkelos und modern sein.
Das Design soll simpel sein. Also Verwendung von wenigen, dezenten Farben (Schattierungen / Blendeffekte erlaubt) und san-serife / simple schrift. Ich würde es mit progressiv, technisch, eher jugendlich, eher offen/frisch, modern, eher prägnant, clean, urban, eher freundschaftlich, schlicht, ehe..
hallo, wir brauchen das design für eine startseite. thema taxi app alle weiteren infos siehe anhang pdf eilauftrag - sofort kauf möglich danke
Unter Flickhafen.de kann das aktuelle Design angeschaut werden. Die Farbe sollten übernommen werden. Über die Startseite kann der Kunde sein Gerät, Service sowie seine Adresse eingeben. Auf der Vergleichsseite bekommt der Kunde die Übersicht welche Reparaturwerkstätten es gibt, zu welch..
Vorweg: Dem Auftrag folgen weitere Teilaufträge an den Gewinner, natürlich gegen Bezahlung. Für die bereits programmierte Webapplikation "tocks" wird ein Design benötigt. Tocks ähnelt den bereits bestehenden Zeiterfassungssystemen, soll sich aber anhand von Einfachheit, Speditivität und..

```html
<!DOCTYPE html>
<html lang="de">
<head>
<meta charset="utf-8">
<title>VeloMarn – Biker App Screens</title>
<link rel="stylesheet" href="https://fonts.googleapis.com/css2?family=Open+Sans:wght@400;600;700&display=swap">
<style>
  :root {
    --page: #ffffff;
    --screen-dark: #1c1c1c;
    --screen-mid: #3a3a3a;
    --panel: #2b2b2b;
    --header: #262626;
    --text: #ffffff;
    --text-soft: #d6d6d6;
    --text-muted: #9a9a9a;
    --button: #8a8a8a;
    --avatar: #9b9b9b;
    --map-city: #e9e4d8;
    --map-green: #cfe3c4;
    --map-region: #efe6cf;
    --map-water: #b9d4ea;
    --ring-teal: #3cc7c7;
    --ring-magenta: #c2247e;
    --ring-green: #43d14b;
    --dot-blue: #62d2f0;
    --online: #3ad13d;
  }
  * { margin: 0; padding: 0; box-sizing: border-box; }
  html, body { width: 1200px; height: 399px; overflow: hidden; background: var(--page); }
  body { position: relative; font-family: "Open Sans", Arial, sans-serif; color: var(--text); }

  .screen {
    position: absolute; top: 33px; width: 185px; height: 329px; overflow: hidden;
    background: var(--screen-dark);
    box-shadow: 6px 8px 14px rgba(0,0,0,0.28);
  }
  .screen--login { left: 34px; }
  .screen--signup { left: 271px; }
  .screen--nearby { left: 507px; }
  .screen--tour { left: 743px; }
  .screen--profile { left: 979px; }

  .backdrop {
    position: absolute; inset: 0;
    background: linear-gradient(180deg, #262626 0%, #4a4a4a 42%, #5a5a5a 52%, #2e2e2e 70%, #1a1a1a 100%);
  }
  .abs { position: absolute; }
  .center { left: 0; right: 0; text-align: center; }

  .brand { font-weight: 700; color: var(--text); letter-spacing: 0.2px; }
  .brand--hero { font-size: 26px; top: 62px; }
  .brand--form { font-size: 19px; top: 30px; }
  .brand--bar { font-size: 13px; left: 15px; }

  .field-label { font-size: 7px; color: var(--text); }
  .field-line { height: 1px; background: var(--text-soft); }

  .pill {
    position: absolute; height: 12px; border-radius: 3px;
    background: var(--button); color: var(--text);
    font-size: 6.6px; line-height: 12px; text-align: center;
  }
  .pill--light { background: #ffffff; color: #222; }
  .link { font-size: 5px; color: var(--text-muted); text-decoration: underline; }

  .topbar { position: absolute; top: 0; left: 0; right: 0; background: var(--header); }
  .menu-icon { position: absolute; right: 14px; width: 14px; }

  .map { position: absolute; left: 0; right: 0; }
  .map--city { top: 27px; height: 214px; background: linear-gradient(135deg, var(--map-city), #ddd8cc 55%, var(--map-green)); }
  .map--region { top: 33px; height: 230px; background: linear-gradient(160deg, var(--map-water) 0%, var(--map-region) 22%, #f1e9d2 60%, #e7dfc4 100%); }

  .panel { position: absolute; left: 0; right: 0; bottom: 0; background: var(--panel); }

  .avatar { position: absolute; border-radius: 50%; background: var(--avatar); }
  .pin { position: absolute; border-radius: 50%; border: 2px solid; background: var(--avatar); }

  .txt { position: absolute; white-space: nowrap; }
  .stars { letter-spacing: 1.5px; }
  .underline { text-decoration: underline; }
</style>
</head>
<body>

<!-- Screen 1: Anmelden -->
<section class="screen screen--login">
  <div class="backdrop" role="img" aria-label="Foto einer leeren Landstraße vor Bergen in Schwarzweiß"></div>
  <div class="abs center brand brand--hero">VeloMarn</div>
  <div class="abs center field-label" style="top:181px">Nickname</div>
  <div class="abs field-line" style="left:34px;width:117px;top:196px"></div>
  <div class="abs center field-label" style="top:214px">Passwort</div>
  <div class="abs field-line" style="left:34px;width:117px;top:229px"></div>
  <div class="pill" style="left:66px;width:54px;top:252px">Anmelden</div>
  <div class="abs center link" style="top:274px">Stattdessen registrieren</div>
</section>

<!-- Screen 2: Registrieren -->
<section class="screen screen--signup">
  <div class="backdrop" role="img" aria-label="Foto einer leeren Landstraße vor Bergen in Schwarzweiß"></div>
  <div class="abs center brand brand--form">VeloMarn</div>
  <div class="abs center field-label" style="top:82px">Nickname</div>
  <div class="abs field-line" style="left:34px;width:117px;top:94px"></div>
  <div class="abs center field-label" style="top:117px">Dein Motorrad</div>
  <div class="abs field-line" style="left:34px;width:117px;top:128px"></div>
  <div class="abs center field-label" style="top:151px">m/w/d</div>
  <div class="abs field-line" style="left:34px;width:117px;top:163px"></div>
  <div class="abs center field-label" style="top:183px">E-Mail</div>
  <div class="abs field-line" style="left:34px;width:117px;top:195px"></div>
  <div class="abs center field-label" style="top:216px">Ort</div>
  <div class="abs field-line" style="left:34px;width:117px;top:228px"></div>
  <div class="abs center field-label" style="top:248px">Geburtsdatum</div>
  <div class="abs field-line" style="left:34px;width:117px;top:260px"></div>
  <div class="pill" style="left:65px;width:55px;top:284px">Registrieren</div>
  <div class="abs center link" style="top:303px">Stattdessen anmelden</div>
</section>

<!-- Screen 3: Biker in der Nähe -->
<section class="screen screen--nearby">
  <div class="topbar" style="height:27px">
    <div class="txt brand brand--bar" style="top:6px">VeloMarn</div>
    <svg class="menu-icon" style="top:8px" viewBox="0 0 14 11" height="11"><rect y="0" width="14" height="2" fill="#fff"/><rect y="4.5" width="14" height="2" fill="#fff"/><rect y="9" width="14" height="2" fill="#fff"/></svg>
  </div>
  <div class="map map--city" role="img" aria-label="Stadtkarte mit Straßen und Grünflächen, rötlicher Umkreis um den eigenen Standort"></div>
  <div class="abs" style="left:22px;top:33px;width:190px;height:190px;border-radius:50%;background:rgba(240,150,150,0.18);border:3px solid rgba(240,150,150,0.35)"></div>
  <div class="pin" role="img" aria-label="Profilfoto eines Bikers" style="left:116px;top:43px;width:40px;height:40px;border-color:var(--ring-teal)"></div>
  <div class="pin" role="img" aria-label="Profilfoto einer Bikerin" style="left:20px;top:114px;width:40px;height:40px;border-color:var(--ring-magenta)"></div>
  <div class="pin" role="img" aria-label="Profilfoto eines Bikers" style="left:132px;top:159px;width:44px;height:44px;border-color:var(--ring-green);box-shadow:0 0 0 2px #fff,0 0 0 3px var(--ring-green)"></div>
  <div class="abs" style="left:102px;top:128px;width:11px;height:11px;border-radius:50%;background:var(--dot-blue);border:1.5px solid #fff"></div>
  <div class="abs" style="left:151px;top:249px;width:0;height:0"></div>
  <div class="abs" style="left:151px;top:220px;width:7px;height:7px;border-radius:50%;background:#2e9e3a;border:1px solid #fff"></div>

  <div class="panel" style="height:88px">
    <div class="avatar" role="img" aria-label="Profilfoto von Nick Nameless" style="left:20px;top:14px;width:38px;height:38px"></div>
    <div class="txt" style="left:70px;top:19px;font-size:7px">Nick Nameless</div>
    <div class="txt stars" style="left:70px;top:27px;font-size:9px">★★★★☆</div>
    <div class="txt" style="left:70px;top:42px;font-size:5px">bereit für eine Tour</div>
    <svg class="abs" style="left:24px;top:60px" width="32" height="10" viewBox="0 0 32 10">
      <circle cx="3.5" cy="6.5" r="3" fill="#fff"/><circle cx="15" cy="6.5" r="3" fill="#fff"/>
      <path d="M3 5 L8 2 L14 2 L17 5 L12 6 Z" fill="#fff"/>
      <path d="M21 5.5 L24 8.5 L30 1.5" stroke="#fff" stroke-width="1.6" fill="none"/>
    </svg>
    <div class="pill" style="left:70px;top:58px;width:54px;height:11px;line-height:11px">Route starten</div>
    <svg class="abs" style="left:143px;top:13px" width="24" height="22" viewBox="0 0 24 22">
      <path d="M2 2 H16 V12 H7 L3 15 V12 H2 Z" fill="none" stroke="#fff" stroke-width="1.6"/>
      <path d="M9 8 H22 V18 H21 V21 L17 18 H9 Z" fill="var(--panel)" stroke="#fff" stroke-width="1.6"/>
      <circle cx="20" cy="3" r="2.5" fill="var(--online)"/>
    </svg>
    <div class="txt underline" style="left:145px;top:38px;font-size:6.6px">Chat</div>
    <div class="txt" style="left:144px;top:47px;font-size:5px">online</div>
  </div>
</section>

<!-- Screen 4: Tour -->
<section class="screen screen--tour">
  <div class="topbar" style="height:33px">
    <div class="txt brand brand--bar" style="top:9px">VeloMarn</div>
    <svg class="menu-icon" style="top:11px" viewBox="0 0 14 11" height="11"><rect y="0" width="14" height="2" fill="#fff"/><rect y="4.5" width="14" height="2" fill="#fff"/><rect y="9" width="14" height="2" fill="#fff"/></svg>
  </div>
  <div class="map map--region" role="img" aria-label="Landkarte Norddeutschland bis Süddeutschland mit blau markierter Tourroute und Fahrzeiten"></div>
  <div class="panel" style="height:66px">
    <div class="txt" style="left:26px;top:14px;font-size:7px">Mitglieder</div>
    <div class="avatar" role="img" aria-label="Profilfoto Mitglied" style="left:14px;top:29px;width:13px;height:13px"></div>
    <div class="avatar" role="img" aria-label="Profilfoto Mitglied" style="left:33px;top:29px;width:13px;height:13px"></div>
    <div class="avatar" role="img" aria-label="Profilfoto Mitglied" style="left:53px;top:29px;width:13px;height:13px"></div>
    <div class="avatar" style="left:73px;top:29px;width:13px;height:13px;background:#eee"></div>
    <svg class="abs" style="left:14px;top:41px" width="70" height="7" viewBox="0 0 70 7">
      <path d="M2 3 L4.5 5.5 L9 1" stroke="#fff" stroke-width="1.5" fill="none"/>
      <path d="M21 3 L23.5 5.5 L28 1" stroke="#fff" stroke-width="1.5" fill="none"/>
      <path d="M41 3 L43.5 5.5 L48 1" stroke="#fff" stroke-width="1.5" fill="none"/>
    </svg>
    <div class="txt" style="left:111px;top:11px;font-size:6.6px">Tourstart: 11:00</div>
    <div class="txt" style="left:111px;top:23px;font-size:6.6px">Treffpunkt: <span class="underline">NSHW</span></div>
    <div class="pill" style="left:119px;top:37px;width:43px">Bereit ✓</div>
  </div>
</section>

<!-- Screen 5: Profil -->
<section class="screen screen--profile">
  <div class="backdrop" role="img" aria-label="Foto einer leeren Landstraße vor Bergen in Schwarzweiß"></div>
  <div class="txt brand brand--bar" style="top:7px;left:12px">VeloMarn</div>
  <svg class="menu-icon" style="top:9px" viewBox="0 0 14 11" height="11"><rect y="0" width="14" height="2" fill="#fff"/><rect y="4.5" width="14" height="2" fill="#fff"/><rect y="9" width="14" height="2" fill="#fff"/></svg>
  <div class="avatar" style="left:21px;top:70px;width:34px;height:34px;background:#e4e4e4"></div>
  <div class="txt" style="left:64px;top:64px;font-size:13px">Nickname</div>
  <div class="txt stars" style="left:64px;top:82px;font-size:14px">★★★★☆</div>
  <svg class="abs" style="left:25px;top:113px" width="26" height="24" viewBox="0 0 24 22">
    <path d="M2 2 H16 V12 H7 L3 15 V12 H2 Z" fill="none" stroke="#fff" stroke-width="1.6"/>
    <path d="M9 8 H22 V18 H21 V21 L17 18 H9 Z" fill="#333" stroke="#fff" stroke-width="1.6"/>
    <circle cx="20" cy="3" r="2.5" fill="var(--online)"/>
  </svg>
  <div class="txt underline" style="left:29px;top:140px;font-size:6.6px">Chat</div>
  <div class="txt" style="left:28px;top:149px;font-size:5px">online</div>
  <svg class="abs" style="left:64px;top:115px" width="30" height="14" viewBox="0 0 30 14">
    <circle cx="5" cy="9" r="4" fill="#fff"/><circle cx="24" cy="9" r="4" fill="#fff"/>
    <path d="M3 7 L10 3 L19 3 L25 7 L17 9 Z" fill="#fff"/>
  </svg>
  <div class="txt" style="left:101px;top:117px;font-size:7px">Supersportler</div>
  <div class="txt underline" style="left:64px;top:133px;font-size:7px">Orvenda R 1000 RS</div>
  <div class="txt" style="left:63px;top:153px;font-size:7px">Gesamte Fahrstrecke:</div>
  <div class="txt" style="left:63px;top:163px;font-size:7px">12.829 km</div>
  <div class="txt" style="left:63px;top:180px;font-size:7px">Schon 10.923 km mit</div>
  <div class="txt" style="left:63px;top:190px;font-size:7px">3Freunden gefahren.</div>
  <div class="pill" style="left:28px;top:219px;width:35px;height:11px;line-height:11px">Freunde</div>
  <div class="pill pill--light" style="left:96px;top:219px;width:63px;height:11px;line-height:11px">Gutschein</div>
  <div class="avatar" role="img" aria-label="Profilfoto Freund" style="left:19px;top:242px;width:13px;height:13px"></div>
  <div class="avatar" role="img" aria-label="Profilfoto Freund" style="left:38px;top:242px;width:13px;height:13px"></div>
  <div class="avatar" role="img" aria-label="Profilfoto Freund" style="left:58px;top:242px;width:13px;height:13px"></div>
</section>

</body>
</html>
```